Background graphic for Vortapex profile

I need a graphic for the background image that appears on Vortapex behind my photo.
I am looking for an image that complements my About Me statement, "Directing patient-first marketing from strategy to execution to help healthcare companies reach the right people at just the right time." I am thinking something with a clock and people and connections. A single example is below and I am open to creative ideas.
1128 (w) x 191 (h) pixels, PNG or JPEG files and have a maximum size of 3MB

```html
<!DOCTYPE html>
<html lang="en">
<head>
<meta charset="utf-8">
<title>Vortapex profile background — patient journey banner</title>
<style>
  :root {
    --stage: #262626;
    --sky-top: #c9e9fb;
    --sky-mid: #e3f2fc;
    --ring: #ffffff;
    --red: #ef4535;
    --orange: #fca61b;
    --lime: #9cc427;
    --green: #4cbf4a;
    --teal: #06b2c8;
    --icon: #ffffff;
  }
  html, body {
    margin: 0;
    width: 1200px;
    height: 1200px;
    overflow: hidden;
    background: var(--stage);
  }
  .banner {
    position: absolute;
    left: 36px;
    top: 481px;
    width: 1128px;
    height: 191px;
    box-shadow: 0 6px 18px rgba(0,0,0,0.55);
    background: linear-gradient(180deg, var(--sky-top) 0%, var(--sky-mid) 70%, var(--sky-top) 100%);
  }
  .banner svg { display: block; }
</style>
</head>
<body>
  <div class="banner">
    <svg class="journey" width="1128" height="191" viewBox="0 0 1128 191" xmlns="http://www.w3.org/2000/svg">
      <defs>
        <linearGradient id="path-hue" gradientUnits="userSpaceOnUse" x1="0" y1="0" x2="1128" y2="0">
          <stop offset="0" stop-color="#ef4535"/>
          <stop offset="0.28" stop-color="#f0442f"/>
          <stop offset="0.34" stop-color="#f7801f"/>
          <stop offset="0.45" stop-color="#fdbf16"/>
          <stop offset="0.52" stop-color="#b3d02a"/>
          <stop offset="0.62" stop-color="#8fc926"/>
          <stop offset="0.68" stop-color="#4cbf4a"/>
          <stop offset="0.76" stop-color="#17c27f"/>
          <stop offset="0.84" stop-color="#08b5a5"/>
          <stop offset="1" stop-color="#06b2c8"/>
        </linearGradient>
        <filter id="lift" x="-30%" y="-30%" width="160%" height="160%">
          <feDropShadow dx="3" dy="4" stdDeviation="3" flood-color="#1a3a55" flood-opacity="0.3"/>
        </filter>
      </defs>

      <path class="journey-line" fill="none" stroke="url(#path-hue)" stroke-width="19"
        d="M0 92 H132 Q150 92 150 110 V163 Q150 181 168 181 H278 Q296 181 296 163 V109 Q296 91 314 91 H379 Q397 91 397 73 V28 Q397 10 415 10 H499 Q517 10 517 28 V94 Q517 112 535 112 H560 Q578 112 578 130 V163 Q578 181 596 181 H674 Q692 181 692 163 V112 Q692 94 710 94 H780 Q798 94 798 76 V28 Q798 10 816 10 H900 Q918 10 918 28 V101 Q918 119 936 119 H1106"/>
      <polygon class="journey-arrow" points="1104,100 1127,118.5 1104,137" fill="var(--teal)"/>

      <!-- Step 1: idea -->
      <g class="step step-idea" transform="translate(111 52)">
        <circle r="43" fill="var(--ring)" filter="url(#lift)"/>
        <circle r="36" fill="var(--red)"/>
        <g fill="none" stroke="var(--icon)" stroke-width="2.2" stroke-linecap="round">
          <path d="M-8 12 Q-8 6 -12 2 A15 15 0 1 1 12 2 Q8 6 8 12 Z"/>
          <path d="M-7 16 H7 M-6 20 H6"/>
          <path d="M0 -25 V-22 M-14 -20 L-12 -18 M14 -20 L12 -18 M-20 -7 H-17 M20 -7 H17"/>
          <circle cy="-6" r="4"/>
          <circle cy="-6" r="8" stroke-dasharray="3 2.3" stroke-width="3"/>
        </g>
      </g>

      <!-- Step 2: timing -->
      <g class="step step-clock" transform="translate(344 135)">
        <circle r="43" fill="var(--ring)" filter="url(#lift)"/>
        <circle r="36" fill="var(--orange)"/>
        <g fill="none" stroke="var(--icon)" stroke-width="2" stroke-linecap="round">
          <path d="M24 -10 A27 27 0 1 1 20 -17"/>
          <path d="M20 -17 L23 -12 L17 -11"/>
          <path d="M0 -22 V-18 M0 22 V18 M-22 0 H-18 M22 0 H18"/>
          <path d="M0 0 L-6 -16 M0 0 H11"/>
          <circle r="2.5"/>
        </g>
      </g>

      <!-- Step 3: people -->
      <g class="step step-people" transform="translate(561 67)">
        <circle r="43" fill="var(--ring)" filter="url(#lift)"/>
        <circle r="36" fill="var(--lime)"/>
        <g fill="var(--icon)">
          <circle cx="-12" cy="-11" r="6"/>
          <path d="M-24 8 Q-23 -2 -12 -3 Q-3 -2 -2 8 Z"/>
          <circle cx="12" cy="-11" r="6"/>
          <path d="M2 8 Q3 -2 12 -3 Q23 -2 24 8 Z"/>
          <circle cx="0" cy="-4" r="7.5" stroke="var(--lime)" stroke-width="2"/>
          <path d="M-14 18 Q-13 5 0 4 Q13 5 14 18 Z" stroke="var(--lime)" stroke-width="2"/>
        </g>
      </g>

      <!-- Step 4: care -->
      <g class="step step-care" transform="translate(740 137)">
        <circle r="43" fill="var(--ring)" filter="url(#lift)"/>
        <circle r="36" fill="var(--green)"/>
        <rect x="-7" y="-22" width="14" height="8" rx="1.5" fill="none" stroke="var(--icon)" stroke-width="2.2"/>
        <rect x="-25" y="-15" width="50" height="35" rx="2.5" fill="var(--icon)"/>
        <path d="M-3 -7 H3 V-1 H9 V5 H3 V11 H-3 V5 H-9 V-1 H-3 Z" fill="var(--green)"/>
      </g>

      <!-- Step 5: process -->
      <g class="step step-process" transform="translate(961 75)">
        <circle r="43" fill="var(--ring)" filter="url(#lift)"/>
        <circle r="36" fill="var(--teal)"/>
        <g fill="none" stroke="var(--icon)" stroke-width="1.6" stroke-linecap="round">
          <circle r="24" stroke-dasharray="6 3.4" stroke-width="5"/>
          <circle r="20"/>
          <path d="M-9 -8 A12 12 0 0 0 8 9"/>
          <path d="M9 8 A12 12 0 0 0 -8 -9"/>
        </g>
      </g>
    </svg>
  </div>
</body>
</html>
```